Musings of Barnaby Quell, 4 time Frostvale Gamer and founding member of the Norwick Sledrun Cl

This is an ebook, available on Pagelume, It is published in a half finished condition. I am going to engage with the online community to expand on chapters, do a foreword, dedication, and also to design the book cover. About one chapter will be added per week until...... The book is 0.99c on Pagelume, buy, read and then design cover, thanks
Target Market(s)
Internet savvy 15-65
Industry/Entity Type
Community
Requirements
Must have
- must work with zephra pagelume self publishing
Nice to have
- Should be colourful graphic, incorporating Jamaica colours
Should not have
- distasteful or obscene
no picture of me on the front
May have a picture for the back cover (if there is such a thing for a digital book)

```html
<!DOCTYPE html>
<html lang="en">
<head>
<meta charset="UTF-8">
<title>Counsel I might have heeded — Barnaby Quell</title>
<link href="https://fonts.googleapis.com/css2?family=Gelasio:ital,wght@1,400;1,700&family=Source+Sans+3:wght@400&display=swap" rel="stylesheet">
<style>
  :root {
    --cover-mustard: #f2b334;
    --title-white: #ffffff;
    --ink: #1c1409;
    --splash-green: #1f8f2a;
    --splash-black: #16120c;
    --splash-orange: #e8831c;
  }
  html, body {
    margin: 0;
    padding: 0;
    overflow: hidden;
    background: #ffffff;
  }
  .cover {
    position: relative;
    width: 752px;
    height: 1200px;
    overflow: hidden;
    background:
      radial-gradient(ellipse at 30% 20%, rgba(255,220,120,0.35), transparent 60%),
      radial-gradient(ellipse at 80% 90%, rgba(180,110,10,0.25), transparent 60%),
      var(--cover-mustard);
  }
  .author {
    position: absolute;
    left: 46px;
    top: 60px;
    margin: 0;
    font-family: "Source Sans 3", "Helvetica Neue", Arial, sans-serif;
    font-weight: 400;
    font-size: 54px;
    letter-spacing: 1.5px;
    line-height: 1;
    color: var(--ink);
    white-space: nowrap;
  }
  .title {
    position: absolute;
    left: 38px;
    top: 142px;
    margin: 0;
    font-family: "Gelasio", Georgia, serif;
    font-style: italic;
    font-weight: 700;
    font-size: 94px;
    line-height: 90px;
    color: var(--title-white);
    white-space: nowrap;
  }
  .subtitle {
    position: absolute;
    left: 40px;
    top: 423px;
    margin: 0;
    font-family: "Gelasio", Georgia, serif;
    font-style: italic;
    font-weight: 400;
    font-size: 42px;
    line-height: 52px;
    color: var(--ink);
    white-space: nowrap;
  }
  .artwork {
    position: absolute;
    left: 0;
    top: 556px;
    width: 752px;
    height: 630px;
  }
</style>
</head>
<body>
  <main class="cover">
    <p class="author">BARNABY QUELL</p>
    <h1 class="title">Counsel<br>I might have<br>heeded.</h1>
    <p class="subtitle">And a few truths<br>I have gathered so far.</p>
    <svg class="artwork" role="img" aria-label="Ink sketch of a four-man bobsleigh crew pushing off, over green, black and orange paint splashes" viewBox="0 0 752 630" xmlns="http://www.w3.org/2000/svg">
      <defs>
        <linearGradient id="splash-tones" x1="0" y1="0" x2="1" y2="0.6">
          <stop offset="0" stop-color="var(--splash-orange)"/>
          <stop offset="0.3" stop-color="var(--splash-green)"/>
          <stop offset="0.6" stop-color="var(--splash-black)"/>
          <stop offset="1" stop-color="var(--splash-orange)" stop-opacity="0.6"/>
        </linearGradient>
      </defs>
      <path d="M0 90 C120 40 220 20 330 50 C430 80 560 40 752 70 L752 200 C650 260 600 340 640 430 C670 500 700 560 660 600 C560 560 470 500 380 470 C260 430 130 420 0 440 Z" fill="url(#splash-tones)" opacity="0.92"/>
    </svg>
  </main>
</body>
</html>
```